Create a Flyer for a Darts Tournament

We need a Flyer for a Darts Tournament that is going to be organized by our darts department (logo attached). The name of the tournament is "3. KLW Dartsturnier". The Flyer should look modern, professional and in a way that everyone can see at the first impression that is has to do with dart sports. The logo of our department should be on the flyer as well. On the flyer we need an area where we can place some informations regarding the tournament (bullet points) etc. And a area where we can place informations regarding the registration progress (e.g. "Registration via E-Mail". Should fit well to our logo.

Target Market(s)

Darts Players for the Tournament

Font styles to use
Serif

Colors

Designer to choose colors to be used in the design.

Requirements
Must have
• Name of the Tournament, our Logo, place for some tournament details, link to our registration page (besucher.tv-halmerau.de). Should

```html
<!DOCTYPE html>
<html lang="de">
<head>
<meta charset="utf-8">
<title>3. KLW Dartsturnier</title>
<link rel="stylesheet" href="https://fonts.googleapis.com/css2?family=Oswald:wght@400;500;600;700&display=swap">
<style>
  :root {
    --blue: #1f5fae;
    --navy: #123565;
    --ink: #141414;
    --black: #0b0b0b;
    --white: #ffffff;
    --paper: #e9eaec;
    --grey: #b9bcc1;
    --muted: #5b5f66;
  }
  * { box-sizing: border-box; margin: 0; padding: 0; }
  html, body { width: 692px; height: 1200px; overflow: hidden; }
  body { font-family: "Oswald", sans-serif; background: var(--paper); color: var(--ink); }
  .flyer { position: relative; width: 692px; height: 1200px; display: flex; flex-direction: column; }

  .hero { position: relative; height: 560px;
    background: radial-gradient(circle at 28% 45%, #6d6f73 0%, #3a3c40 28%, #1c1d20 60%, #0e0f11 100%); }
  .hero-photo { position: absolute; inset: 0; }
  .club-mark { position: absolute; top: 26px; right: 26px; width: 124px; height: 124px;
    background: var(--navy); display: flex; align-items: center; justify-content: center;
    color: var(--white); font-weight: 700; font-size: 44px; letter-spacing: 2px; }

  .headline { display: flex; height: 210px; }
  .title-block { width: 58%; background: var(--navy); color: var(--white);
    display: flex; align-items: center; padding: 0 26px; gap: 18px;
    border-top: 6px solid var(--blue); }
  .edition { font-size: 150px; font-weight: 700; line-height: 1; }
  .title-text { display: flex; flex-direction: column; gap: 6px; }
  .club-name { font-size: 52px; font-weight: 700; line-height: 0.95; }
  .event-name { font-size: 30px; font-weight: 600; line-height: 1; letter-spacing: 1px; }
  .badge { align-self: flex-start; background: var(--white); color: var(--navy);
    font-size: 16px; font-weight: 600; padding: 2px 10px; letter-spacing: 1px; }
  .subline { font-size: 15px; letter-spacing: 2px; font-weight: 500; }
  .subline b { font-weight: 700; }

  .date-block { flex: 1; background: var(--white); display: flex; flex-direction: column;
    align-items: center; justify-content: center; border-top: 6px solid var(--blue); }
  .day { color: var(--blue); font-size: 96px; font-weight: 700; line-height: 0.9; }
  .day sup { font-size: 38px; vertical-align: top; }
  .weekday { font-size: 40px; font-weight: 700; letter-spacing: 2px; line-height: 1.1; }
  .month { border: 2px solid var(--blue); color: var(--blue); font-size: 18px;
    font-weight: 600; letter-spacing: 2px; padding: 2px 14px; margin-top: 4px; }

  .venue { height: 56px; background: var(--grey); display: flex; align-items: center;
    padding: 0 26px; font-size: 24px; font-weight: 700; letter-spacing: 1px; color: var(--ink); }

  .details { flex: 1; background: var(--paper); display: grid;
    grid-template-columns: 1fr 1fr; gap: 0 30px; padding: 30px 26px; align-content: center; }
  .details ul { list-style: none; display: flex; flex-direction: column; gap: 12px; }
  .details li { font-size: 22px; font-weight: 400; letter-spacing: 1px; }
  .details li b { font-weight: 700; color: var(--navy); margin-right: 6px; }

  .registration { height: 170px; background: var(--black); padding: 34px 26px;
    display: flex; flex-direction: column; gap: 16px; }
  .reg-row { display: flex; height: 58px; }
  .reg-label { background: var(--blue); color: var(--white); font-weight: 700; font-size: 26px;
    letter-spacing: 2px; display: flex; align-items: center; padding: 0 22px; }
  .reg-link { flex: 1; background: var(--white); color: var(--ink); font-weight: 600;
    font-size: 24px; letter-spacing: 1px; display: flex; align-items: center; padding: 0 20px;
    text-transform: uppercase; }
  .info-link { color: var(--white); font-size: 18px; letter-spacing: 2px; text-transform: uppercase; }
  .info-link b { font-weight: 700; }
</style>
</head>
<body>
<main class="flyer">
  <section class="hero">
    <div class="hero-photo" role="img" aria-label="Photo of a steel dartboard on the left and a player throwing a dart on the right, dark monochrome tones"></div>
    <div class="club-mark">KLW</div>
  </section>

  <section class="headline">
    <div class="title-block">
      <span class="edition">3</span>
      <div class="title-text">
        <span class="club-name">KLW</span>
        <span class="event-name">DARTSTURNIER</span>
        <span class="badge">KEINE LIGASPIELER</span>
        <span class="subline"><b>STEEL DARTS</b> HOBBYTURNIER</span>
      </div>
    </div>
    <div class="date-block">
      <span class="day">25<sup>th</sup></span>
      <span class="weekday">SONNTAG</span>
      <span class="month">JANUARY | 2025</span>
    </div>
  </section>

  <div class="venue">SVZ IN 75123 HALMERAU</div>

  <section class="details">
    <ul>
      <li><b>SAMSTAG</b>25.01.2025</li>
      <li><b>EINLASS</b>16:00 UHR</li>
      <li><b>TURNIERBEGINN</b>17:00 UHR</li>
    </ul>
    <ul>
      <li><b>MAXIMAL</b>48 TEILNEHMER</li>
      <li><b>GRUPPENPHASE</b>301 | DO | BO3</li>
      <li><b>KO-PHASE</b>501 | DO | BO5</li>
    </ul>
  </section>

  <section class="registration">
    <div class="reg-row">
      <span class="reg-label">ANMELDUNG</span>
      <span class="reg-link">besucher.tv-halmerau.de</span>
    </div>
    <p class="info-link"><b>Infos:</b> darts.tv-halmerau.de</p>
  </section>
</main>
</body>
</html>
```